Product Line - Label & Logo design

Logo & label design for a supplement line we are developing . The product name is VORSEN ( gxt ) We would like a white jar with a purple metalic lid and somehow blend in the lettering/wording . I will attach sample products to view. Feel free to add in the boxes of the label with the numbers from the sample label. We can correct once we have the design completed. Feel free to change the lettering style, shape etc

Target Market(s)

Supplement / exercise

Industry/Entity Type

Fitness

Colors
6B429C
8869AF
B7A5CE
E3DAEB
F3F0F8

```html
<!DOCTYPE html>
<html lang="en">
<head>
<meta charset="utf-8">
<title>VORSEN Pre Workout Label</title>
<link rel="stylesheet" href="https://fonts.googleapis.com/css2?family=Exo+2:ital,wght@0,800;1,800;1,900&family=Montserrat:wght@400;600&family=Roboto+Condensed:wght@400;700&display=swap">
<style>
  :root {
    --purple: #9a10b2;
    --purple-bright: #b01dc9;
    --purple-deep: #7a0a8e;
    --ink: #0c0c0e;
    --white: #ffffff;
    --accent: #e6e01e;
    --page: #ffffff;
  }
  html, body {
    margin: 0;
    width: 864px;
    height: 1200px;
    overflow: hidden;
    background: var(--page);
  }
  .label {
    position: absolute;
    left: 32px;
    top: 383px;
    width: 800px;
    height: 433px;
    display: block;
  }
  .display { font-family: "Exo 2", sans-serif; font-weight: 900; font-style: italic; }
  .brand { font-family: "Exo 2", sans-serif; font-weight: 800; font-style: normal; fill: var(--white); letter-spacing: 2px; }
  .body-copy { font-family: "Montserrat", sans-serif; fill: var(--white); }
  .heading-small { font-family: "Montserrat", sans-serif; font-weight: 600; fill: var(--purple-bright); }
  .facts { font-family: "Roboto Condensed", sans-serif; fill: #111; }
  .facts-bold { font-weight: 700; }
</style>
</head>
<body>
<svg class="label" viewBox="0 0 878 475" xmlns="http://www.w3.org/2000/svg" role="img" aria-label="VORSEN pre workout label">
  <defs>
    <linearGradient id="bodyShade" x1="0" y1="0" x2="1" y2="1">
      <stop offset="0" stop-color="#151518"/>
      <stop offset="1" stop-color="#08080a"/>
    </linearGradient>
  </defs>

  <!-- label body -->
  <rect class="label-body" x="0" y="0" width="878" height="475" fill="url(#bodyShade)"/>

  <!-- top band -->
  <polygon class="top-band" points="0,0 542,0 517,73 0,73" fill="var(--purple)"/>
  <g class="top-stripes" fill="var(--purple-bright)">
    <polygon points="548,0 566,0 552,45 534,45"/>
    <polygon points="576,0 594,0 580,45 562,45"/>
    <polygon points="604,0 622,0 608,45 590,45"/>
    <polygon points="632,0 650,0 636,45 618,45"/>
    <polygon points="660,0 678,0 664,45 646,45"/>
    <polygon points="688,0 706,0 692,45 674,45"/>
    <polygon points="716,0 734,0 720,45 702,45"/>
    <polygon points="744,0 762,0 748,45 730,45"/>
    <polygon points="772,0 790,0 776,45 758,45"/>
    <polygon points="800,0 818,0 804,45 786,45"/>
  </g>
  <text class="brand" x="410" y="54" font-size="34" text-anchor="middle">VORSEN</text>

  <!-- bottom band -->
  <polygon class="bottom-band" points="402,400 878,400 878,475 380,475" fill="var(--purple)"/>
  <g class="bottom-stripes" fill="var(--purple-bright)">
    <polygon points="40,428 56,428 44,475 28,475"/>
    <polygon points="66,428 82,428 70,475 54,475"/>
    <polygon points="92,428 108,428 96,475 80,475"/>
    <polygon points="118,428 134,428 122,475 106,475"/>
    <polygon points="144,428 160,428 148,475 132,475"/>
    <polygon points="170,428 186,428 174,475 158,475"/>
    <polygon points="196,428 212,428 200,475 184,475"/>
    <polygon points="222,428 238,428 226,475 210,475"/>
    <polygon points="248,428 264,428 252,475 236,475"/>
    <polygon points="274,428 290,428 278,475 262,475"/>
    <polygon points="300,428 316,428 304,475 288,475"/>
    <polygon points="326,428 342,428 330,475 314,475"/>
    <polygon points="352,428 368,428 356,475 340,475"/>
  </g>

  <!-- supplement facts panel -->
  <g class="supplement-facts">
    <rect x="58" y="110" width="174" height="213" rx="6" fill="var(--white)"/>
    <rect x="62" y="114" width="166" height="205" rx="3" fill="none" stroke="#111" stroke-width="0.8"/>
    <text class="facts facts-bold" x="66" y="135" font-size="15.5" textLength="158">SUPPLEMENT FACTS</text>
    <line x1="66" y1="139" x2="224" y2="139" stroke="#111" stroke-width="1"/>
    <text class="facts" x="66" y="146" font-size="4.5">Serving Size 1 scoop (6.5 g)</text>
    <text class="facts" x="66" y="152" font-size="4.5">Servings Per Container 30</text>
    <line x1="66" y1="156" x2="224" y2="156" stroke="#111" stroke-width="2"/>
    <text class="facts" x="150" y="162" font-size="4" text-anchor="end">Amount Per Serving</text>
    <text class="facts" x="224" y="162" font-size="4" text-anchor="end">% Daily Value</text>
    <line x1="66" y1="165" x2="224" y2="165" stroke="#111" stroke-width="0.6"/>
    <g class="facts" font-size="4.3">
      <text class="facts-bold" x="66" y="172">Calories</text><text x="182" y="172" text-anchor="end">5</text>
      <text class="facts-bold" x="66" y="180">Total Carbohydrate</text><text x="182" y="180" text-anchor="end">1 g</text><text x="224" y="180" text-anchor="end">&lt;1%*</text>
      <text class="facts-bold" x="66" y="188">L-Citrulline</text><text x="182" y="188" text-anchor="end">9000 mg</text><text x="224" y="188" text-anchor="end">**</text>
      <text class="facts-bold" x="66" y="196">Creatine Monohydrate</text><text x="182" y="196" text-anchor="end">3000 mg</text><text x="224" y="196" text-anchor="end">**</text>
      <text class="facts-bold" x="66" y="204">Beta-Alanine</text><text x="182" y="204" text-anchor="end">3000 mg</text><text x="224" y="204" text-anchor="end">**</text>
      <text class="facts-bold" x="66" y="212">Betaine Anhydrous</text><text x="182" y="212" text-anchor="end">2500 mg</text><text x="224" y="212" text-anchor="end">**</text>
      <text x="70" y="220">L-Leucine</text><text x="182" y="220" text-anchor="end">2000 mg</text><text x="224" y="220" text-anchor="end">**</text>
      <text x="70" y="228">L-Isoleucine</text><text x="182" y="228" text-anchor="end">1000 mg</text><text x="224" y="228" text-anchor="end">**</text>
      <text x="70" y="236">L-Valine</text><text x="182" y="236" text-anchor="end">1000 mg</text><text x="224" y="236" text-anchor="end">**</text>
      <text class="facts-bold" x="66" y="244">Taurine</text><text x="182" y="244" text-anchor="end">1000 mg</text><text x="224" y="244" text-anchor="end">**</text>
      <text class="facts-bold" x="66" y="252">Caffeine Anhydrous</text><text x="182" y="252" text-anchor="end">277 mg</text><text x="224" y="252" text-anchor="end">**</text>
    </g>
    <line x1="66" y1="256" x2="224" y2="256" stroke="#111" stroke-width="1.5"/>
    <text class="facts" x="66" y="262" font-size="3.8">**Daily Value not established.</text>
    <text class="facts" x="66" y="274" font-size="4.3"><tspan class="facts-bold">OTHER INGREDIENTS:</tspan> Natural and artificial flavors,</text>
    <text class="facts" x="66" y="280" font-size="4.3">citric acid, sucralose.</text>
  </g>

  <!-- other ingredients -->
  <text class="heading-small" x="60" y="347" font-size="8">OTHER INGREDIENTS</text>
  <g class="body-copy" font-size="8.3">
    <text x="60" y="361">Artificial Flavors, Polydextrose, Citric</text>
    <text x="60" y="372">Acid, Malic Acid, Calcium Silicate, Silicon</text>
    <text x="60" y="383">Dioxide, Sucralose, Acesulfame</text>
    <text x="60" y="394">Potassium</text>
  </g>

  <!-- centre title -->
  <text class="display" x="468" y="200" font-size="118" fill="var(--white)" text-anchor="middle" textLength="290" lengthAdjust="spacingAndGlyphs">PRE</text>
  <polygon class="workout-band" points="312,205 600,205 588,252 300,252" fill="var(--purple)"/>
  <text class="display" x="447" y="244" font-size="44" fill="var(--white)" text-anchor="middle" textLength="270" lengthAdjust="spacingAndGlyphs">WORKOUT</text>
  <text class="display" x="456" y="281" font-size="23" fill="var(--purple-bright)" stroke="var(--purple-deep)" stroke-width="0.6" text-anchor="middle" textLength="190" lengthAdjust="spacingAndGlyphs">PERFORMANCE</text>
  <text class="display" x="456" y="303" font-size="23" fill="var(--purple-bright)" stroke="var(--purple-deep)" stroke-width="0.6" text-anchor="middle" textLength="140" lengthAdjust="spacingAndGlyphs">RECOVERY</text>

  <!-- stat badges -->
  <g class="stat-badges">
    <g>
      <polygon points="314,314 372,314 367,349 309,349" fill="var(--accent)"/>
      <polygon points="312,312 370,312 365,346 307,346" fill="var(--purple)"/>
      <text class="display" x="339" y="334" font-size="19" fill="var(--white)" text-anchor="middle">9<tspan font-size="11">G</tspan></text>
      <text class="display" x="338" y="342" font-size="5.5" fill="var(--white)" text-anchor="middle">CITRULLINE</text>
    </g>
    <g>
      <polygon points="382,314 440,314 435,349 377,349" fill="var(--accent)"/>
      <polygon points="380,312 438,312 433,346 375,346" fill="var(--purple)"/>
      <text class="display" x="407" y="334" font-size="19" fill="var(--white)" text-anchor="middle">3<tspan font-size="11">G</tspan></text>
      <text class="display" x="406" y="342" font-size="5.5" fill="var(--white)" text-anchor="middle">CREATINE</text>
    </g>
    <g>
      <polygon points="450,314 508,314 503,349 445,349" fill="var(--accent)"/>
      <polygon points="448,312 506,312 501,346 443,346" fill="var(--purple)"/>
      <text class="display" x="475" y="334" font-size="19" fill="var(--white)" text-anchor="middle">277<tspan font-size="9">MG</tspan></text>
      <text class="display" x="474" y="342" font-size="5.5" fill="var(--white)" text-anchor="middle">CAFFEINE</text>
    </g>
    <g>
      <polygon points="518,314 576,314 571,349 513,349" fill="var(--accent)"/>
      <polygon points="516,312 574,312 569,346 511,346" fill="var(--purple)"/>
      <text class="display" x="543" y="334" font-size="19" fill="var(--white)" text-anchor="middle">3<tspan font-size="11">G</tspan></text>
      <text class="display" x="542" y="342" font-size="5.5" fill="var(--white)" text-anchor="middle">BETA-ALANINE</text>
    </g>
  </g>

  <text class="body-copy" x="452" y="379" font-size="11.5" text-anchor="middle">DIETARY SUPPLEMENT</text>
  <text class="body-copy" x="452" y="392" font-size="11.5" text-anchor="middle">NET WT 195g (6.9 OZ)</text>

  <!-- servings -->
  <text class="brand" x="474" y="440" font-size="44" text-anchor="middle" letter-spacing="1">30</text>
  <text class="display" x="472" y="455" font-size="12" fill="var(--white)" text-anchor="middle" letter-spacing="1">SERVINGS</text>

  <!-- directions -->
  <text class="heading-small" x="670" y="117" font-size="8">DIRECTIONS</text>
  <g class="body-copy" font-size="8.4">
    <text x="670" y="131">Take one serving (1 level scoop) of</text>
    <text x="670" y="142">VORSEN, mixed with 6 fl. oz of water,</text>
    <text x="670" y="153">20-30 minutes before training. Some</text>
    <text x="670" y="164">individuals may experience a harmless</text>
    <text x="670" y="175">tingling sensation, which is attributable</text>
    <text x="670" y="186">to Beta-Alanine. Use only as directed.</text>
  </g>
  <text class="heading-small" x="670" y="210" font-size="8">NOTE</text>
  <g class="body-copy" font-size="8.4">
    <text x="670" y="224">Please do not use in combination with</text>
    <text x="670" y="235">other dietary supplements,</text>
    <text x="670" y="246">pharmaceuticals, foods that are</text>
    <text x="670" y="257">considered to be stimulants.</text>
  </g>

  <!-- side panel brand -->
  <text class="brand" x="733" y="392" font-size="30" text-anchor="middle">VORSEN</text>
  <text class="display" x="736" y="441" font-size="25" fill="var(--white)" text-anchor="middle" textLength="210" lengthAdjust="spacingAndGlyphs">PRE WORKOUT</text>
</svg>
</body>
</html>
```